Velvet & Bloom Hair Extensions needs a business card

We need a business card designed for an online luxury hair extensions business called Velvet & Bloom, we already have a logo and need an innovative business card (2-sided preferably). The strap line for the brand is 'Luxury Hair At Every Touchpoint!'. The brand is a premium brand selling virgin hair extensions and the target market is the mid-affluent ethnic woman as such the design should reflect this. The brand logo is grey and can be sent when requested.

Target Market(s)

25 to 35 year mid-affluent ethnic woman (Afro-American, Mixed Race, Asian)

Industry/Entity Type

Hair

Colors

Designer to choose colors to be used in the design.

Requirements
Must have
• Business Name: Velvet and Bloom
Strapline: Luxury hair at every touchpoint!
Domain: ​www.velvetandbloom-demo.com
Email: info@velvetandbloom-demo.com
sales and enquiries
44 07391 xxxxxxx

Please use the grey main brand logo depicted in page 2 of the attached pdf document

```html
<!DOCTYPE html>
<html lang="en">
<head>
<meta charset="utf-8">
<title>Velvet and Bloom – Business Card</title>
<link href="https://fonts.googleapis.com/css2?family=Fondamento&display=swap" rel="stylesheet">
<style>
  :root {
    --paper-light: #ffffff;
    --paper-mist: #e6e6e6;
    --panel-grey: #b4b4b4;
    --panel-mid: #a2a2a2;
    --panel-dark: #4a4a4a;
    --edge-teal: #8fa5a7;
    --ink: #151515;
    --brand-grey: #9a9a9a;
  }
  html, body {
    margin: 0;
    padding: 0;
    width: 1200px;
    height: 704px;
    overflow: hidden;
    background: #ffffff;
  }
  .card {
    position: relative;
    width: 1200px;
    height: 704px;
    overflow: hidden;
    font-family: "Fondamento", "Papyrus", fantasy;
    color: var(--ink);
  }
  .card-background {
    position: absolute;
    inset: 0;
    width: 100%;
    height: 100%;
  }
  .brand-mark {
    position: absolute;
    left: 62px;
    top: 300px;
    display: flex;
    align-items: center;
    gap: 12px;
  }
  .brand-mark__square {
    width: 22px;
    height: 22px;
    background: var(--brand-grey);
  }
  .brand-mark__name {
    font-size: 26px;
    letter-spacing: 2px;
    color: var(--brand-grey);
    text-transform: uppercase;
  }
  .business-name {
    position: absolute;
    left: 303px;
    top: 104px;
    margin: 0;
    font-size: 60px;
    font-weight: 400;
    line-height: 1;
  }
  .strapline {
    position: absolute;
    left: 307px;
    top: 200px;
    margin: 0;
    font-size: 37px;
    line-height: 1;
  }
  .contact {
    position: absolute;
    left: 636px;
    top: 432px;
    margin: 0;
    font-style: normal;
  }
  .contact__email {
    font-size: 31px;
    line-height: 1;
    display: block;
  }
  .contact__label {
    font-size: 31px;
    line-height: 1;
    display: block;
    margin-top: 24px;
  }
  .contact__phone {
    font-size: 28px;
    line-height: 1;
    display: block;
    margin-top: 12px;
  }
  .website {
    position: absolute;
    left: 489px;
    top: 624px;
    margin: 0;
    font-size: 20px;
  }
</style>
</head>
<body>
  <div class="card">
    <svg class="card-background" viewBox="0 0 1200 704" preserveAspectRatio="none" aria-hidden="true">
      <defs>
        <radialGradient id="mist-glow" cx="0.18" cy="0.35" r="0.7">
          <stop offset="0" stop-color="var(--paper-light)"/>
          <stop offset="0.6" stop-color="#f2f2f2"/>
          <stop offset="1" stop-color="var(--paper-mist)"/>
        </radialGradient>
        <linearGradient id="panel-shade" x1="0" y1="0" x2="1" y2="1">
          <stop offset="0" stop-color="#c4c4c4"/>
          <stop offset="0.6" stop-color="var(--panel-grey)"/>
          <stop offset="1" stop-color="var(--panel-mid)"/>
        </linearGradient>
        <linearGradient id="edge-glow" x1="0" y1="0" x2="1" y2="0">
          <stop offset="0" stop-color="var(--edge-teal)" stop-opacity="0"/>
          <stop offset="0.5" stop-color="var(--edge-teal)" stop-opacity="0.7"/>
          <stop offset="1" stop-color="var(--edge-teal)" stop-opacity="0"/>
        </linearGradient>
      </defs>
      <rect class="bg-paper" width="1200" height="704" fill="url(#mist-glow)"/>
      <polygon class="bg-diagonal-panel" points="540,0 1200,0 1200,704 250,704" fill="url(#panel-shade)"/>
      <polygon class="bg-diagonal-edge" points="520,0 580,0 290,704 230,704" fill="url(#edge-glow)"/>
      <polygon class="bg-upper-fold" points="560,0 1200,0 1200,420" fill="#cdcdcd" opacity="0.45"/>
      <polygon class="bg-dark-corner" points="1200,520 1200,704 840,704" fill="var(--panel-dark)"/>
      <line class="bg-dark-edge" x1="1200" y1="516" x2="834" y2="704" stroke="var(--edge-teal)" stroke-width="4" opacity="0.6"/>
    </svg>

    <div class="brand-mark">
      <span class="brand-mark__square"></span>
      <span class="brand-mark__name">Velvet &amp; Bloom</span>
    </div>

    <h1 class="business-name">Velvet and Bloom</h1>
    <p class="strapline">Luxury hair at every touchpoint!</p>

    <address class="contact">
      <span class="contact__email">Email: info@velvetandbloom-demo.com</span>
      <span class="contact__label">Sales and Enquiries</span>
      <span class="contact__phone">44 07391 xxxxxxx</span>
    </address>

    <p class="website">www.velvetandbloom-demo.com</p>
  </div>
</body>
</html>
```